Yoga class opening. Little schedule for JUNE JULY and AUGUST

Flyer to promote an opening yoga class. The color of the docx haven't to be respected.

We want something joyfull, professional, clean and serious.

About the logo we oppened a contest at the same time so at the moment there is no logo but the logo color will be simple.

The phone number will change so you can poste a random one for the design that i can change by myself.

i recieved many creation in both side BUT i want something in 1 side :)

Target Market(s)

Yoga student. all age

Industry/Entity Type

It Professional

Logo Text

Yoga fern

Font styles to use
Sans Serif

Requirements
Must have
• The text present on the docx
Nice to have
• Some symbols about yoga ( Namasté signs, mandala, ... )
Should not have
• Not too much details it has to be clear.

```html
<!DOCTYPE html>
<html lang="fr">
<head>
<meta charset="utf-8">
<title>Yoga fern – Stages d'été</title>
<link rel="stylesheet" href="https://fonts.googleapis.com/css2?family=Alegreya:ital,wght@0,400;1,400;1,500&family=Lato:ital,wght@1,900&family=Open+Sans:wght@300;400&family=Arimo:wght@400;700&family=Oswald:wght@400&display=swap">
<style>
  :root{
    --orange:#f18d4f;
    --orange-deep:#ef7f3c;
    --blue:#3aa6da;
    --link-blue:#2f5aa8;
    --ink:#333333;
    --rule:#c9c9c9;
    --logo-grey:#8f9091;
    --page:#ffffff;
  }
  *{margin:0;padding:0;box-sizing:border-box}
  html,body{width:1200px;height:1000px;overflow:hidden;background:var(--page)}
  .flyer{position:absolute;left:283px;top:50px;width:636px;height:898px;background:#fff;box-shadow:0 4px 14px rgba(0,0,0,.18);overflow:hidden}
  .hero{position:absolute;left:0;top:0;width:636px;height:308px;
    background:linear-gradient(90deg,#f19a5f 0%,#f3a36d 40%,#e8b98f 62%,#d9c2a8 78%,#cfc0b0 100%)}
  .ribbon{position:absolute;left:27px;top:35px;width:268px;height:60px}
  .ribbon-label{position:absolute;left:27px;top:35px;width:268px;height:60px;line-height:60px;text-align:center;
    font:italic 900 25px/60px "Lato",sans-serif;color:#fff;letter-spacing:3px}
  .logo-box{position:absolute;left:494px;top:30px;width:121px;height:54px;background:var(--logo-grey);
    color:#fff;font:400 14px/54px "Arimo",sans-serif;text-align:center}
  .hero-title{position:absolute;left:28px;top:122px;font:italic 900 25px/31px "Lato",sans-serif;color:#fff;letter-spacing:4.5px;
    text-shadow:0 2px 4px rgba(0,0,0,.25)}
  .hero-lead{position:absolute;left:28px;top:194px;width:300px;font:italic 400 13.5px/23px "Alegreya",serif;color:#fff;letter-spacing:1px}
  .month{position:absolute;height:24px;border-radius:12px;background:var(--blue);color:#fff;
    font:italic 400 19px/24px "Alegreya",serif;text-align:center;box-shadow:3px 3px 4px rgba(0,0,0,.15)}
  .course{position:absolute}
  .course-title{font:italic 500 19px/22px "Alegreya",serif;color:var(--orange)}
  .course-price{font:300 18px/22px "Open Sans",sans-serif;color:var(--ink);margin-top:3px}
  .dates{list-style:none;margin-top:6px;font:400 8.5px/15px "Arimo",sans-serif;color:var(--ink)}
  .rule{position:absolute;left:29px;width:576px;height:1px;background:var(--rule)}
  .info{position:absolute;left:347px}
  .launch{top:708px;font:700 9.5px/12px "Arimo",sans-serif;color:var(--ink)}
  .contact{top:738px;left:347px;display:flex;gap:9px}
  .contact-mark{width:38px;height:38px;background:var(--link-blue);flex:none}
  .contact-text{font:700 12px/15px "Arimo",sans-serif;color:var(--ink)}
  .contact-text .lead{color:var(--link-blue)}
  .farewell{top:795px;font:400 21px/26px "Oswald",sans-serif;color:var(--orange);letter-spacing:4px}
  .footer{position:absolute;left:0;bottom:0;width:636px;height:46px;background:var(--orange);color:#fff;
    font:400 12px/46px "Arimo",sans-serif;text-align:center;letter-spacing:2px}
</style>
</head>
<body>
<main class="flyer">
  <header class="hero" role="img" aria-label="Photo d'un cours de yoga : une élève souriante, mains jointes, devant un groupe en méditation, sous un voile orangé"></header>
  <svg class="ribbon" viewBox="0 0 268 60" aria-hidden="true">
    <polygon points="0,0 268,0 252,30 268,60 0,60 16,30" fill="#fff"/>
    <polygon points="10,5 258,5 245,30 258,55 10,55 23,30" fill="var(--orange-deep)"/>
  </svg>
  <div class="ribbon-label">NOUVEAU!!</div>
  <div class="logo-box">Yoga fern</div>
  <h1 class="hero-title">VOTRE STUDIO<br>DE YOGA A IXELLES</h1>
  <p class="hero-lead">En attendant le planning des cours de la rentrée, YOGA FERN vous propose ses stages et ateliers d'été.</p>

  <div class="month" style="left:36px;top:338px;width:109px">JUIN</div>
  <section class="course" style="left:45px;top:374px">
    <h2 class="course-title">Stage découverte du YOGA</h2>
    <p class="course-price">10h00 85 €</p>
    <ul class="dates">
      <li>Du lundi 6 au vendredi 10 juin : 10h00 à 12h00 ou 18h00 à 20h00</li>
      <li>Du lundi 13 au vendredi 17 juin : 10h00 à 12h00 ou 18h00 à 20h00</li>
      <li>Du lundi 20 au vendredi 24 juin : 10h00 à 12h00 ou 18h00 à 20h00</li>
      <li>Du lundi 27 au vendredi 1er juillet : 10h00 à 12h00 ou 18h00 à 20h00</li>
    </ul>
  </section>
  <section class="course" style="left:347px;top:354px">
    <h2 class="course-title">Atelier gestion du stress yoga/<br>sophrologie</h2>
    <p class="course-price">2h00 28 €</p>
    <ul class="dates">
      <li>Samedi 11 juin 10h30 à 12h30</li>
      <li>Samedi 11 juin 15h à 17h00</li>
      <li>Dimanche 12 juin 10h30 à 12h30</li>
      <li>Dimanche 12 juin 14h à 16h00</li>
    </ul>
  </section>
  <div class="rule" style="top:508px"></div>

  <div class="month" style="left:38px;top:522px;width:110px">JUILLET</div>
  <section class="course" style="left:45px;top:558px">
    <h2 class="course-title">Stage initiation à l'ASHTANGA</h2>
    <p class="course-price">10h00 85 €</p>
    <ul class="dates">
      <li>Du lundi 4 au vendredi 8 juillet : 10h00 à 12h00 ou 18h00 à 20h00</li>
      <li>Du lundi 11 au vendredi 15 juillet : 10h00 à 12h00 ou 18h00 à 20h00</li>
      <li>Du lundi 18 au vendredi 22 juillet : 10h00 à 12h00 ou 18h00 à 20h00</li>
      <li>Du lundi 25 au vendredi 29 juillet : 10h00 à 12h00 ou 18h00 à 20h00</li>
    </ul>
  </section>
  <section class="course" style="left:347px;top:540px">
    <h2 class="course-title">Atelier gestion du stress yoga/<br>sophrologie</h2>
    <p class="course-price">2h00 28 €</p>
    <ul class="dates">
      <li>Samedi 9 juillet 10h30 à 12h30</li>
      <li>Samedi 9 juillet 15h00 à 17h00</li>
      <li>Dimanche 10 juillet 10h30 à 12h30</li>
      <li>Dimanche 10 juillet 14h00 à 16h00</li>
    </ul>
  </section>
  <div class="rule" style="top:682px"></div>

  <div class="month" style="left:38px;top:698px;width:110px">AOUT</div>
  <section class="course" style="left:45px;top:727px">
    <h2 class="course-title">Stage découverte du YOGA</h2>
    <p class="course-price">10h00 85 €</p>
    <ul class="dates">
      <li>Du lundi 1er au vendredi 5 août : 10h00 à 12h00 ou 18h00 à 20h00</li>
      <li>Du lundi 8 au vendredi 12 août : 10h00 à 12h00 ou 18h00 à 20h00</li>
      <li>Du lundi 15 au vendredi 19 août : 10h00 à 12h00 ou 18h00 à 20h00</li>
      <li>Du lundi 22 au vendredi 26 août : 10h00 à 12h00 ou 18h00 à 20h00</li>
    </ul>
  </section>

  <p class="info launch">Démarrage du planning annuel le 5 septembre 2016</p>
  <div class="info contact">
    <span class="contact-mark" aria-hidden="true"></span>
    <p class="contact-text"><span class="lead">Plus d'info et inscription :</span><br>Ou via notre page Friendline :<br>www.friendline.com/yoga fern</p>
  </div>
  <p class="info farewell">UN BEL ETE A TOUS !</p>

  <footer class="footer">212 RUE DES TILLEULS 1050 IXELLES</footer>
</main>
</body>
</html>
```